Simple landing page/Web presence for boutique Fund Manager, Verran Capital

We need a website presence for our funds management business. All we need is a simple landing page with some "text" about us and a link /button to our Fund Due diligence portal. the "text" we would like to see is: "Verran Capital Pty Ltd. Its Trustee is Bellmont Trust Partners Ltd - also based in Sydney. Bellmont is the holder of an Australian Financial Services License (no.731205) whilst Verran Capital operates under a Corporate Authorised Representation from Bellmont."

We have the attached logo

```html
<!DOCTYPE html>
<html lang="en">
<head>
<meta charset="utf-8">
<title>Verran Capital — Boutique Fund Manager</title>
<link rel="stylesheet" href="https://fonts.googleapis.com/css2?family=Montserrat:wght@400;500;600;800;900&family=Open+Sans:wght@700;800&family=Fira+Sans+Extra+Condensed:wght@300&display=swap">
<style>
  :root {
    --ink: #000000;
    --paper: #ffffff;
    --charcoal: #1a1a1a;
    --footer: #0e0e0e;
    --field-line: #3a3a3a;
    --label-grey: #7a7a7a;
    --blob-edge: #454545;
  }
  html, body {
    margin: 0;
    padding: 0;
    width: 1200px;
    height: 2873px;
    overflow: hidden;
    background: var(--paper);
  }
  .page {
    position: relative;
    width: 1200px;
    height: 2873px;
    font-family: "Montserrat", sans-serif;
    color: var(--ink);
  }
  .abs { position: absolute; }

  /* Top bar */
  .top-bar {
    left: 0; top: 0; width: 1200px; height: 89px;
    background: linear-gradient(180deg, #2a2a2a 0%, #111 70%, #050505 100%);
    border-bottom: 3px solid #3c3c3c;
  }
  .top-bar__name {
    left: 0; width: 1200px; top: 30px;
    text-align: center;
    font-weight: 600; font-size: 22px; color: var(--paper);
    letter-spacing: 1px;
  }

  /* Hero */
  .hero {
    left: 0; top: 91px; width: 1200px; height: 589px;
    background: linear-gradient(100deg, #cfc6bd 0%, #f1efec 30%, #f6f5f3 48%, #bdb3aa 62%, #4a4a4e 78%, #e5e2de 100%);
  }
  .hero__brand {
    left: 0; width: 960px; top: 190px;
    text-align: center;
    font-weight: 600; font-size: 44px; letter-spacing: 1px;
  }
  .hero__title {
    left: 0; width: 960px;
    text-align: center;
    font-weight: 900; font-size: 32px;
  }
  .hero__title--one { top: 296px; }
  .hero__title--two { top: 359px; }
  .btn-solid {
    left: 317px; top: 449px; width: 329px; height: 67px;
    background: var(--ink); color: var(--paper);
    font-family: "Open Sans", sans-serif; font-weight: 800; font-size: 25px;
    display: flex; align-items: center; justify-content: center;
  }
  .scroll-hint {
    left: 0; width: 1200px; top: 604px;
    text-align: center;
    font-size: 21px; letter-spacing: 2px; color: #111;
  }

  /* About band */
  .about {
    left: 0; top: 680px; width: 1200px; height: 518px;
    background: radial-gradient(ellipse at 50% 40%, #2c2c2c 0%, #151515 60%, #070707 100%);
    color: var(--paper);
    text-align: center;
  }
  .about__heading {
    position: absolute; left: 0; width: 1200px; top: 62px;
    font-weight: 500; font-size: 31px; margin: 0;
  }
  .about__body {
    position: absolute; left: 300px; width: 600px; top: 110px;
    font-weight: 600; font-size: 23.5px; line-height: 42.2px; margin: 0;
  }
  .btn-outline {
    position: absolute; left: 436px; top: 391px; width: 325px; height: 63px;
    border: 2px solid var(--paper);
    display: flex; align-items: center; justify-content: center;
    font-weight: 800; font-size: 25px;
  }

  /* Callback */
  .callback__title {
    left: 46px; top: 1346px;
    font-family: "Open Sans", sans-serif; font-weight: 800; font-size: 41px;
    margin: 0; letter-spacing: 0.5px;
  }
  .field {
    left: 47px; width: 546px; height: 40px;
    border-bottom: 3px solid var(--field-line);
    display: flex; align-items: flex-end; gap: 10px;
    padding-bottom: 4px;
  }
  .field svg { flex: none; }
  .field__label {
    font-family: "Open Sans", sans-serif; font-weight: 700; font-size: 21px;
    color: var(--label-grey); line-height: 1;
  }
  .btn-submit {
    left: 47px; top: 1869px; width: 319px; height: 75px;
    background: var(--ink); color: var(--paper); border-radius: 6px;
    font-family: "Open Sans", sans-serif; font-weight: 800; font-size: 33px;
    display: flex; align-items: center; justify-content: center;
  }
  .team-photo { left: 638px; top: 1336px; }

  /* Brand strip */
  .brand-strip {
    left: 0; top: 2141px; width: 589px; height: 368px;
    background: var(--ink);
  }
  .brand-strip__name {
    position: absolute; left: 0; width: 589px; top: 152px;
    text-align: center;
    font-weight: 600; font-size: 50px; color: var(--paper); letter-spacing: 2px;
  }
  .analytics-photo {
    left: 589px; top: 2141px; width: 611px; height: 368px;
    background: linear-gradient(120deg, #4a4a4a 0%, #9a9a96 22%, #e9ecee 45%, #f4f5f6 70%, #c9ccd0 100%);
  }

  /* Footer */
  .footer {
    left: 0; top: 2509px; width: 1200px; height: 364px;
    background: var(--footer);
    border-top: 1px solid #3a3a3a;
    color: var(--paper);
  }
  .footer__contact {
    position: absolute; top: 98px;
    font-family: "Fira Sans Extra Condensed", sans-serif; font-weight: 300;
    font-size: 39px; letter-spacing: -1.5px; white-space: nowrap;
    transform: translateX(-50%);
  }
  .footer__sep {
    position: absolute; top: 102px; width: 2px; height: 40px; background: var(--paper);
  }
  .footer__nav {
    position: absolute; top: 254px;
    font-size: 17px; letter-spacing: 2px; white-space: nowrap;
    transform: translateX(-50%);
  }
</style>
</head>
<body>
<div class="page">

  <header class="abs top-bar">
    <div class="abs top-bar__name">Verran Capital</div>
  </header>

  <section class="abs hero" role="img" aria-label="Photo of smiling business colleagues in conversation at a meeting">
    <div class="abs hero__brand">Verran Capital</div>
    <div class="abs hero__title hero__title--one">Verran Capital</div>
    <div class="abs hero__title hero__title--two">Boutique Fund Manager</div>
    <div class="abs btn-solid">CONTACT US</div>
    <div class="abs scroll-hint" style="top:513px">Scroll Down For More</div>
    <svg class="abs" style="left:590px; top:545px" width="20" height="44" viewBox="0 0 20 44">
      <circle cx="10" cy="9" r="7" fill="none" stroke="#111" stroke-width="1.6"/>
      <line x1="10" y1="16" x2="10" y2="44" stroke="#111" stroke-width="1.6"/>
    </svg>
  </section>

  <section class="abs about">
    <h2 class="about__heading">Verran Capital Pty Ltd.</h2>
    <p class="about__body">Its Trustee is Bellmont Trust Partners Ltd also based in Sydney. Bellmont is the holder of an Australian Financial Services License (no.731205)&nbsp; whilst Verran Capital operates under a Corporate Authorised Representation from Bellmont."</p>
    <div class="btn-outline">VIEW DUE DILIGENCE</div>
  </section>

  <h2 class="abs callback__title">GET A CALLBACK</h2>

  <div class="abs field" style="top:1450px">
    <svg width="26" height="34" viewBox="0 0 26 34" fill="none" stroke="#555" stroke-width="1.8">
      <circle cx="13" cy="9" r="6"/>
      <path d="M2 32 V26 Q2 19 13 19 Q24 19 24 26 V32 Z"/>
      <path d="M13 19 V28"/>
    </svg>
    <span class="field__label">YOUR NAME</span>
  </div>

  <div class="abs field" style="top:1555px">
    <svg width="28" height="30" viewBox="0 0 28 30" fill="none" stroke="#555" stroke-width="1.8">
      <path d="M2 11 L14 2 L26 11 V28 H2 Z"/>
      <path d="M2 11 L14 20 L26 11"/>
      <circle cx="14" cy="12" r="3.5"/>
    </svg>
    <span class="field__label">YOUR EMAIL ADRESS</span>
  </div>

  <div class="abs field" style="top:1658px">
    <svg width="28" height="28" viewBox="0 0 28 28" fill="none" stroke="#555" stroke-width="1.8">
      <path d="M6 2 L11 8 L8 12 Q11 18 16 20 L20 17 L26 22 L22 26 Q10 26 2 8 Z"/>
    </svg>
    <span class="field__label">CONTACT NUMBER</span>
  </div>

  <div class="abs field" style="top:1757px">
    <svg width="28" height="26" viewBox="0 0 28 26" fill="none" stroke="#555" stroke-width="1.8">
      <path d="M2 2 H20 V14 H9 L4 18 V14 H2 Z"/>
      <path d="M20 8 H26 V20 H24 V24 L19 20 H10 V14"/>
    </svg>
    <span class="field__label">MESSAGE(OPTIONAL)</span>
  </div>

  <div class="abs btn-submit">SUBMIT</div>

  <svg class="abs team-photo" width="562" height="627" viewBox="0 0 562 627" role="img" aria-label="Photo of two women working at a computer in an office">
    <defs>
      <linearGradient id="teamTones" x1="0" y1="0" x2="1" y2="1">
        <stop offset="0" stop-color="#6a6560"/>
        <stop offset="0.45" stop-color="#3d4a52"/>
        <stop offset="0.75" stop-color="#24343d"/>
        <stop offset="1" stop-color="#6f8b8c"/>
      </linearGradient>
    </defs>
    <path d="M562 6 C470 -6 380 4 290 58 C150 142 4 238 2 360 C0 472 120 560 330 600 C430 618 510 626 562 622 Z" fill="var(--blob-edge)"/>
    <path d="M562 18 C474 8 388 18 300 70 C166 150 30 244 30 360 C30 462 140 544 336 586 C432 604 510 612 562 610 Z" fill="url(#teamTones)"/>
  </svg>

  <section class="abs brand-strip">
    <div class="brand-strip__name">Verran Capital</div>
  </section>
  <div class="abs analytics-photo" role="img" aria-label="Photo of a hand with a stylus pointing at analytics charts on a tablet screen"></div>

  <footer class="abs footer">
    <div class="footer__contact" style="left:200px">phone: 1800 4720 615</div>
    <div class="footer__sep" style="left:380px"></div>
    <div class="footer__contact" style="left:608px">E-mail: contact@verrancapital.com</div>
    <div class="footer__sep" style="left:832px"></div>
    <div class="footer__contact" style="left:1007px">info@verrancapital.com</div>

    <div class="footer__nav" style="left:354px">HOME</div>
    <div class="footer__nav" style="left:435px">|</div>
    <div class="footer__nav" style="left:568px">DUE DILIGENCE</div>
    <div class="footer__nav" style="left:698px">|</div>
    <div class="footer__nav" style="left:813px">CONTACT US</div>
  </footer>

</div>
</body>
</html>
```